Manufacturing and engineering company needs corporate stationary

Looking for professional stationary to use internally as well as for giveaways for customers. Looking for digital and printed options.

The logo file attached has the overall colour scheme and the logo needs to be used in the stationary. The circle portion of the logo can be used independently. We are open to variations on the colours and style of logo but it should remain very similar to the attached.

Font styles to use
Serif
Sans Serif

Requirements
Must have
• The logo or at the very least the circle portion of the logo
Nice to have
• Would like a powerpoint template, word document template for proposals, printed brochure template
Should not have
• Business cards are not the focus, while you can suggest ideas this is not the focus

```html
<!DOCTYPE html>
<html lang="en">
<head>
<meta charset="utf-8">
<title>Altrenby Letterhead</title>
<link rel="stylesheet" href="https://fonts.googleapis.com/css2?family=Open+Sans:wght@400;700&display=swap">
<style>
  :root {
    --backdrop: #e2dac6;
    --paper: #fdfdf8;
    --gold: #b08d2e;
    --gold-dark: #9a7a22;
    --steel: #8f8f96;
    --ink: #6d6d72;
    --ghost: #f1f0ea;
  }
  * { box-sizing: border-box; margin: 0; padding: 0; }
  html, body { width: 1200px; height: 784px; overflow: hidden; }
  body {
    background: var(--backdrop);
    font-family: "Open Sans", Arial, sans-serif;
    position: relative;
  }
  .letterhead {
    position: absolute;
    left: 362px; top: 44px;
    width: 476px; height: 696px;
    background: var(--paper);
    box-shadow: 0 2px 8px rgba(0,0,0,0.12);
    overflow: hidden;
  }
  .header-rule { position: absolute; top: 40px; left: 0; right: 0; height: 3px; }
  .header-rule .steel { position: absolute; left: 0; width: 64px; height: 3px; background: var(--steel); }
  .header-rule .gold { position: absolute; left: 168px; right: 18px; height: 3px; background: var(--gold); }
  .brand {
    position: absolute; top: 30px; left: 70px;
    display: flex; align-items: center; gap: 5px;
  }
  .brand-dot { width: 16px; height: 16px; border-radius: 50%; background: var(--gold); }
  .brand-name { font-weight: 700; font-size: 13px; line-height: 16px; color: var(--steel); }
  .contact {
    position: absolute; top: 54px; right: 22px; text-align: right;
    font-style: normal;
    color: var(--ink); font-size: 6.5px; line-height: 10px; letter-spacing: 0.6px;
  }
  .contact .company {
    font-size: 10px; line-height: 14px; font-weight: 700; color: var(--gold);
    letter-spacing: 2px; margin-bottom: 2px;
  }
  .contact .company span { font-weight: 400; }
  .contact .icon {
    display: inline-block; width: 7px; height: 7px; border: 0.8px solid var(--ink);
    border-radius: 50%; vertical-align: -1px; margin: 0 2px 0 6px;
  }
  .contact .icon:first-child { margin-left: 0; }
  .footer-band {
    position: absolute; left: 0; right: 0; bottom: 4px; height: 8px;
    background: var(--gold); border-top: 1px solid var(--gold-dark);
  }
  .ghost-mark {
    position: absolute; left: 0; right: 0; bottom: 50px;
    display: flex; flex-direction: column; align-items: center; gap: 14px;
  }
  .ghost-circle { width: 150px; height: 150px; border-radius: 50%; border: 10px solid var(--ghost); }
  .ghost-name { font-weight: 700; font-size: 62px; line-height: 70px; color: var(--ghost); }
</style>
</head>
<body>
  <main class="letterhead">
    <div class="header-rule"><span class="steel"></span><span class="gold"></span></div>
    <div class="brand">
      <span class="brand-dot"></span>
      <span class="brand-name">Altrenby</span>
    </div>
    <address class="contact">
      <p class="company">ALTREN <span>by</span></p>
      <p><span class="icon"></span>Suite 4, 12 Kestrel Rd, Milford 0000</p>
      <p><span class="icon"></span>00 3141 5920<span class="icon"></span>00 3141 5934<span class="icon"></span>0000 314 159</p>
    </address>
    <div class="ghost-mark" aria-hidden="true">
      <span class="ghost-circle"></span>
      <span class="ghost-name">Altrenby</span>
    </div>
    <div class="footer-band"></div>
  </main>
</body>
</html>
```